Business Card

Designs by L&M Renata Kowalczyk Signature Collection business card
Looking for a modern, classic and timeless business card for our jewelry company

Front of card should be a, all purple solid color for the background and white lettering like the attached document.

On the front of card:
Designs by L&M
Renata Kowalczyk Signature Collection
One of A Kind Designs for you!

Renata Fairbury
Owner

On the back on card
Email: LMDesigns27@postvela.com
Facebook: https://www.facepage-example.com/DesignsbyLMRenataandHolly
Twitter:
https://chirpline-example.com/DesignsbyLM27
Instagram: http://picstream-example.com/DesignsbyLMjewelry

Industry/Entity Type

Business

```html
<!DOCTYPE html>
<html lang="en">
<head>
<meta charset="utf-8">
<title>Designs by L&amp;M – Business Card</title>
<link rel="stylesheet" href="https://fonts.googleapis.com/css2?family=Questrial&family=Mulish:wght@700&display=swap">
<style>
  :root {
    --backdrop: #2f3d43;
    --purple: #6a46a1;
    --purple-deep: #5d3b93;
    --white: #ffffff;
    --grey: #a3a3a3;
    --grey-light: #c9c9c9;
  }
  * { box-sizing: border-box; margin: 0; padding: 0; }
  html, body {
    width: 1200px; height: 1000px; overflow: hidden;
    background: var(--backdrop);
    font-family: "Questrial", "Century Gothic", sans-serif;
  }
  .canvas {
    position: relative; width: 1200px; height: 1000px;
    display: flex; flex-direction: column; align-items: center;
    justify-content: center; gap: 56px;
  }
  .card {
    width: 720px; height: 411px; position: relative; overflow: hidden;
    box-shadow: 0 14px 30px rgba(0,0,0,.35);
  }
  /* Back card */
  .card--back { background: var(--purple); }
  .back-brand {
    height: 196px; background: var(--white);
    display: flex; flex-direction: column; align-items: center;
    padding-top: 30px; color: var(--grey);
  }
  .brand-mark {
    width: 46px; height: 46px; border-radius: 50%;
    background: var(--grey-light); margin-bottom: 12px;
  }
  .brand-name { font-size: 34px; letter-spacing: 5px; line-height: 1; }
  .brand-sub { font-size: 19px; margin-top: 4px; line-height: 1.1; }
  .brand-est { font-size: 19px; letter-spacing: 2px; line-height: 1.1; }
  .contact-list {
    list-style: none; padding: 18px 0 0 64px; color: var(--white);
    font-size: 21px; line-height: 1.28;
  }
  .contact-list li { display: flex; align-items: center; gap: 10px; }
  .contact-icon { width: 20px; height: 20px; flex: none; }
  .contact-dot {
    width: 18px; height: 18px; border-radius: 3px; background: var(--white); flex: none;
  }
  /* Front card */
  .card--front {
    background: radial-gradient(ellipse at 50% 40%, var(--purple) 0%, var(--purple-deep) 100%);
    color: var(--white);
    display: flex; flex-direction: column; align-items: center;
    padding-top: 34px;
  }
  .card--front .brand-mark { width: 62px; height: 62px; background: var(--grey-light); margin-bottom: 18px; }
  .card--front .brand-name { font-size: 38px; letter-spacing: 6px; }
  .card--front .brand-sub { font-size: 22px; }
  .card--front .brand-est { font-size: 22px; }
  .tagline-row { display: flex; align-items: center; gap: 16px; margin-top: 26px; }
  .flourish { width: 58px; height: 12px; background: rgba(255,255,255,.55); border-radius: 6px; }
  .tagline { font-size: 27px; }
  .owner { margin-top: 46px; font-size: 27px; }
  .owner-name { font-family: "Mulish", "Century Gothic", sans-serif; font-weight: 700; font-size: 34px; }
</style>
</head>
<body>
<main class="canvas">
  <section class="card card--back" aria-label="Card back">
    <div class="back-brand">
      <div class="brand-mark"></div>
      <p class="brand-name">DESIGNS BY L&amp;M</p>
      <p class="brand-sub">Renata Kowalczyk Signature Collection</p>
      <p class="brand-est">EST. 2014</p>
    </div>
    <ul class="contact-list">
      <li>
        <svg class="contact-icon" viewBox="0 0 20 20" aria-hidden="true">
          <rect x="1.5" y="4" width="17" height="12" fill="none" stroke="#fff" stroke-width="1.6"/>
          <polyline points="1.5,4 10,11 18.5,4" fill="none" stroke="#fff" stroke-width="1.6"/>
        </svg>
        LMDesigns27@postvela.com
      </li>
      <li><span class="contact-dot"></span>facepage-example.com/DesignsbyLMRenataandHolly</li>
      <li><span class="contact-dot"></span>chirpline-example.com/DesignsbyLM27</li>
      <li><span class="contact-dot"></span>picstream-example.com/DesignsbyLMjewelry</li>
    </ul>
  </section>

  <section class="card card--front" aria-label="Card front">
    <div class="brand-mark"></div>
    <p class="brand-name">DESIGNS BY L&amp;M</p>
    <p class="brand-sub">Renata Kowalczyk Signature Collection</p>
    <p class="brand-est">EST. 2014</p>
    <div class="tagline-row">
      <span class="flourish" role="img" aria-label="Decorative scroll flourish"></span>
      <p class="tagline">One of A Kind Designs for you!</p>
      <span class="flourish" role="img" aria-label="Decorative scroll flourish"></span>
    </div>
    <p class="owner"><span class="owner-name">Renata Fairbury</span> Owner</p>
  </section>
</main>
</body>
</html>
```